We need a website that entices australia's workers to sign up to help protect their industry and their jobs. The key message is "Building a Stronger Australia" and that headline / tagline should feature prominently on the site.

In terms of style I lack the current 'scrolling' style (see example http://www.pebblelane.ca )

The site must dynamically for mobile platforms. It must also use Joomla or Wordpress as CMS so is client editable.

The attached logo is the basis for the design and the name of the organisation is the Enduring Progress Council. Please make an allowance for an iframe embed (min height 650px) see attached sample.

It should also have a subscriber sign up for that connects with Mailing Beacon

Attached text for front page is DRAFT ONLY

Target Market(s)

Working class australians, (eg miners, farmers, factory workers, etc)

Industry/Entity Type

Industry

Coding

Coded - Design and coding required

Number of Pages Required

4 page

Requirements
Must have
• An editable CMS
• Subscription form connecting with Mailing Beacon (see https://kelvoram.postriver.com/help/topic.aspx?t=13)
• Must resize for mobile
• Must allow for an iframe
Nice to have
• It must have a friendly feel but strong, not 'girly' though should not alienate women
Should not have
• Images that are not australian
• Images that do not have the appropriate rights to use

```html
<!DOCTYPE html>
<html lang="en">
<head>
<meta charset="utf-8">
<title>Building A Stronger Australia — Enduring Progress Council</title>
<link rel="stylesheet" href="https://fonts.googleapis.com/css2?family=Open+Sans:wght@400;600;700&family=Noto+Serif:wght@700&display=swap">
<style>
:root{
  --hero-sky:#3c7fb8;
  --hero-sand:#c7a58a;
  --nav-bg:#111111;
  --nav-link:#f3a32b;
  --flame:#e5512a;
  --flame-deep:#d8431f;
  --steel:#2b3f57;
  --steel-light:#4a5f77;
  --amber:#ec7b22;
  --amber-light:#f08c2c;
  --cta:#fbb52b;
  --cta-text:#2a1a06;
  --paper:#f4f4f4;
  --field-line:#d6d6d6;
  --muted:#8b8b8b;
  --ink:#333333;
  --sky-btn:#2e9fd8;
  --teal:#1f8fa4;
  --navy:#2b4870;
  --footer:#151515;
  --footer-text:#8a8a8a;
  --footer-head:#e0e0e0;
  --subscribe:#e8502a;
  --white:#ffffff;
}
*{box-sizing:border-box;margin:0;padding:0}
html,body{width:1200px;height:3121px;overflow:hidden}
body{font-family:"Open Sans",Arial,sans-serif;color:var(--white);background:var(--footer);position:relative}
section,header,nav,footer{position:absolute;left:0;width:1200px}

.hero{top:0;height:627px;overflow:hidden}
.hero-photo{position:absolute;inset:0;background:linear-gradient(180deg,var(--hero-sky) 0%,#6aa4cf 40%,var(--hero-sand) 75%,#8a6a58 100%)}
.brand{position:absolute;left:0;width:1200px;top:120px;text-align:center;font-size:26px;font-weight:600;color:var(--white);letter-spacing:1px}
.brand-dot{display:inline-block;width:22px;height:22px;border-radius:50%;background:var(--amber);vertical-align:-4px;margin-right:12px}
.hero-title{position:absolute;left:0;width:1200px;top:385px;text-align:center;font-size:52px;font-weight:400;letter-spacing:3px;word-spacing:10px;text-shadow:0 2px 6px rgba(0,0,0,.5)}

.site-nav{top:627px;height:29px;background:var(--nav-bg)}
.site-nav a{position:absolute;top:4px;font-family:"Noto Serif",Georgia,serif;font-weight:700;font-size:15px;color:var(--nav-link);text-decoration:none}
.site-nav .sep{position:absolute;top:3px;color:var(--nav-link);font-size:16px}

.family{top:656px;height:423px;background:linear-gradient(135deg,var(--flame) 0%,var(--flame-deep) 55%,var(--flame) 100%);text-align:center}
.family h2{position:absolute;top:56px;width:100%;font-size:50px;font-weight:600}
.family p{position:absolute;top:160px;width:100%;font-size:26px;line-height:34px}
.btn{position:absolute;display:block;background:var(--cta);color:var(--cta-text);text-decoration:none;text-align:center;border-radius:3px}
.family .btn{left:430px;top:314px;width:293px;height:29px;line-height:29px;font-size:16px}

.greenies{top:1079px;height:484px;background:linear-gradient(90deg,var(--steel) 0%,var(--steel-light) 50%,var(--steel) 100%);text-align:center}
.greenies h2{position:absolute;top:82px;left:200px;width:800px;font-size:33px;font-weight:400;line-height:40px}
.greenies h2 .big{display:block;font-size:54px;line-height:70px;margin-top:4px}
.greenies p{position:absolute;top:295px;left:210px;width:780px;font-size:17px;line-height:24px}

.tell{top:1563px;height:526px;background:linear-gradient(180deg,var(--amber-light),var(--amber))}
.tell h2{position:absolute;top:52px;left:200px;width:800px;text-align:center;font-size:30px;font-weight:600;line-height:36px}
.reasons{position:absolute;left:208px;top:200px;list-style:none}
.reasons li{position:relative;padding-left:48px;font-size:24px;line-height:31px;margin-bottom:19px;width:680px}
.reasons li svg{position:absolute;left:0;top:0}

.email-bank{top:2089px;height:414px;background:var(--paper);color:var(--ink)}
.bank-form{position:absolute;left:208px;top:16px;width:370px}
.bank-form h3{font-size:20px;font-weight:400;border-left:2px solid #bbb;padding-left:8px;margin-bottom:16px;color:#444}
.bank-form .intro{font-size:10px;line-height:14px;color:#666;margin-bottom:8px}
.field{display:block;width:364px;height:27px;border:1px solid var(--field-line);background:var(--white);font-size:10px;color:#999;padding:0 8px;line-height:26px;margin-bottom:18px;position:relative}
.field.select::after{content:"";position:absolute;right:8px;top:11px;border:4px solid transparent;border-top-color:#333}
.form-actions{text-align:right;width:364px;margin-top:-4px}
.form-actions span{display:inline-block;border:1px solid #999;background:#eee;font-size:10px;padding:1px 6px;border-radius:2px;margin-left:4px}
.action-card{position:absolute;top:125px;width:180px;text-align:center}
.action-card h4{font-size:14px;font-weight:600;margin:8px 0 4px;color:#333}
.action-card p{font-size:10px;line-height:13px;color:#666;height:28px}
.action-card .pill{display:block;margin:8px auto 0;width:112px;height:25px;line-height:25px;background:var(--sky-btn);color:var(--white);font-size:11px;border-radius:3px}

.get-started{top:2503px;height:305px;background:linear-gradient(180deg,var(--navy),#365887);text-align:center}
.get-started h2{position:absolute;top:84px;width:100%;font-size:33px;font-weight:600}
.get-started p{position:absolute;top:146px;left:220px;width:760px;font-size:17px;line-height:26px}
.get-started .btn{left:468px;top:240px;width:210px;height:33px;line-height:33px;font-size:18px}

.site-footer{top:2808px;height:277px;background:var(--footer);color:var(--footer-text);font-size:11px}
.col{position:absolute;top:64px}
.col h4{font-size:15px;font-weight:400;color:var(--footer-head);margin-bottom:14px}
.col p{line-height:15px;margin-bottom:16px}
.col ul{list-style:none}
.col li{line-height:27px}
.sub-field{display:block;width:200px;height:25px;border:1px solid #444;background:#1e1e1e;margin-bottom:15px}
.subscribe{display:inline-block;background:var(--subscribe);color:var(--white);padding:0 12px;height:25px;line-height:25px;font-size:11px}
.legal{top:3085px;height:36px;background:#0b0b0b;color:#555;font-size:10px;padding:12px 208px}
</style>
</head>
<body>

<header class="hero">
  <div class="hero-photo" role="img" aria-label="Photo of a smiling Australian family at the beach under a blue sky"></div>
  <div class="brand"><span class="brand-dot"></span>Enduring Progress Council</div>
  <h1 class="hero-title">Building A Stronger Australia</h1>
</header>

<nav class="site-nav">
  <a href="#" style="left:275px">Take Action</a><span class="sep" style="left:385px">/</span>
  <a href="#" style="left:437px">About</a><span class="sep" style="left:533px">/</span>
  <a href="#" style="left:571px">Facts</a><span class="sep" style="left:640px">/</span>
  <a href="#" style="left:685px">News</a><span class="sep" style="left:764px">/</span>
  <a href="#" style="left:806px">Contact</a>
</nav>

<section class="family">
  <h2>My family comes first</h2>
  <p>I care for the environment – but not at the cost of my job,<br>our savings or our retirement</p>
  <a class="btn" href="#">Take action to protect your family</a>
</section>

<section class="greenies" role="img" aria-label="Muted photo of mining and industrial machinery behind the text">
  <h2>The Greenies want your bank and your super fund to stop investing in mining, agriculture and other industries that are the backbone of <span class="big">Australia</span></h2>
  <p>While they are trying to ‘do good’ if they are successful their actions will severely impact the lives of everyday Australians. Any loss of investment in Australian industries WILL have knock on effects for you, your family and your community.</p>
</section>

<section class="tell">
  <h2>Tell your bank and super fund you do NOT want them to divest out of Australian industry. Tell them you want to keep Australia strong</h2>
  <ul class="reasons">
    <li><svg width="34" height="34" viewBox="0 0 34 34"><polygon points="17,2 30,9.5 30,24.5 17,32 4,24.5 4,9.5" fill="none" stroke="#fbd3a8" stroke-width="2"/><polygon points="17,9 24,13 24,21 17,25 10,21 10,13" fill="none" stroke="#fbd3a8" stroke-width="2"/></svg>Cost you your job as less investment means less jobs</li>
    <li><svg width="34" height="34" viewBox="0 0 34 34"><polygon points="17,2 30,9.5 30,24.5 17,32 4,24.5 4,9.5" fill="none" stroke="#fbd3a8" stroke-width="2"/><polygon points="17,9 24,13 24,21 17,25 10,21 10,13" fill="none" stroke="#fbd3a8" stroke-width="2"/></svg>Give you less to retire on as your superannuation fund gets strong returns from investment</li>
    <li><svg width="34" height="34" viewBox="0 0 34 34"><polygon points="17,2 30,9.5 30,24.5 17,32 4,24.5 4,9.5" fill="none" stroke="#fbd3a8" stroke-width="2"/><polygon points="17,9 24,13 24,21 17,25 10,21 10,13" fill="none" stroke="#fbd3a8" stroke-width="2"/></svg>Reduce your hard earned savings</li>
    <li><svg width="34" height="34" viewBox="0 0 34 34"><polygon points="17,2 30,9.5 30,24.5 17,32 4,24.5 4,9.5" fill="none" stroke="#fbd3a8" stroke-width="2"/><polygon points="17,9 24,13 24,21 17,25 10,21 10,13" fill="none" stroke="#fbd3a8" stroke-width="2"/></svg>Impact communities that rely on industry</li>
    <li><svg width="34" height="34" viewBox="0 0 34 34"><polygon points="17,2 30,9.5 30,24.5 17,32 4,24.5 4,9.5" fill="none" stroke="#fbd3a8" stroke-width="2"/><polygon points="17,9 24,13 24,21 17,25 10,21 10,13" fill="none" stroke="#fbd3a8" stroke-width="2"/></svg>Not help the environment at all</li>
  </ul>
</section>

<section class="email-bank">
  <div class="bank-form">
    <h3>Email your Bank - it's easy</h3>
    <p class="intro">Take a few moments to contact your bank and let them know you do not want them to divest from Australian industry. Here's your opportunity to be heard. Your voice will make a difference.</p>
    <p class="intro">To get started please fill in your name and email address:</p>
    <span class="field">First Name</span>
    <span class="field">Family Name</span>
    <span class="field">email</span>
    <span class="field select">Select Bank</span>
    <span class="field select">Super Fund</span>
    <div class="form-actions"><span>Submit</span><span>Cancel</span></div>
  </div>

  <div class="action-card" style="left:640px">
    <svg width="54" height="54" viewBox="0 0 54 54"><rect x="6" y="12" width="34" height="34" fill="none" stroke="#1f8fa4" stroke-width="3"/><polyline points="14,28 24,38 48,6" fill="none" stroke="#1f8fa4" stroke-width="5"/></svg>
    <h4>Register to Vote</h4>
    <p>Register to vote by October 6th and make your voice be heard</p>
    <span class="pill">Learn More</span>
  </div>
  <div class="action-card" style="left:821px">
    <svg width="54" height="54" viewBox="0 0 54 54"><circle cx="22" cy="16" r="10" fill="none" stroke="#1f8fa4" stroke-width="2"/><circle cx="22" cy="14" r="3.5" fill="#1f8fa4"/><path d="M16,23 a6,5 0 0 1 12,0" fill="#1f8fa4"/><circle cx="34" cy="36" r="13" fill="none" stroke="#1f8fa4" stroke-width="2"/><circle cx="34" cy="33" r="4.5" fill="#1f8fa4"/><path d="M26,45 a8,7 0 0 1 16,0" fill="#1f8fa4"/></svg>
    <h4>Community Connect</h4>
    <p>Join our online community to connect with others nearby</p>
    <span class="pill">Join Now</span>
  </div>
</section>

<section class="get-started" role="img" aria-label="Blue-tinted photo of a city skyline behind the call to action">
  <h2>It's easy to get started</h2>
  <p>We have developed an advocacy centre — a place where you can send a letter or email to your bank, super fund, MP or your newspaper, share information online with your friends via social media.</p>
  <a class="btn" href="#">Get it Now !</a>
</section>

<footer class="site-footer">
  <div class="col" style="left:208px;width:300px">
    <h4>About us</h4>
    <p>We say what we do, we do what<br>we say, and we're looking forward to prove it to you.</p>
    <p>14 Quarry Lane, Ballarat, Australia</p>
    <p>(03) 5550 0142</p>
    <p>hello@firmgroundvoice.org</p>
  </div>
  <div class="col" style="left:544px">
    <h4>Latest Posts</h4>
    <ul>
      <li>Home - Basic</li>
      <li>Mission and Vision</li>
      <li>Shortcode System</li>
      <li>List Styles</li>
      <li>About us</li>
      <li>Offline Page</li>
    </ul>
  </div>
  <div class="col" style="left:752px">
    <h4>Join our Mailing List</h4>
    <span class="sub-field"></span>
    <span class="sub-field"></span>
    <span class="subscribe">Subscribe</span>
  </div>
</footer>

<div class="legal" style="position:absolute;left:0;width:1200px">© 2013 Enduring Progress Council. All rights reserved.</div>

</body>
</html>
```